Baseball Themed Birthday Invitation

Hello,

I need a birthday invitation design created for me. I will be taking the design, getting it manufactured in bulk and selling them.

These types of invitations are not custom, but rather will have "fill in fields". Please see attachment as an example (wild one example attached). The mandatory fill in fields are : Name, Location, Date, Time, RSVP.

The target age will be 4-12

The size is 7" x 5".

This project is for a Baseball themed party design. I attached an example invitation (baseball design) to show one i really like. This design does not include the fill in fields, but i like the use of fonts/colors design. That being said, I am open to seeing different concepts and designs.

Thank you!

Target Market(s)

Boys 4-12 years old

Requirements
Must have
• Fill in fields as discussed in brief.

```html
<!DOCTYPE html>
<html lang="en">
<head>
<meta charset="UTF-8">
<title>Baseball Birthday Invitation</title>
<link rel="stylesheet" href="https://fonts.googleapis.com/css2?family=Alfa+Slab+One&family=Comfortaa:wght@500&family=Sacramento&display=swap">
<style>
  :root {
    --navy: #2a4a75;
    --backdrop: #2d4f7b;
    --backdrop-light: #3a6090;
    --red: #d13127;
    --ticket-edge: #e9edf0;
    --tan: #dcc3a1;
    --tan-dark: #cdb08a;
    --cream: #f0e0c9;
    --band: #3d6190;
    --white: #ffffff;
    --ball-light: #f7f0e4;
    --ball-shade: #e4d6c0;
    --bat-light: #c8a889;
    --bat-shade: #e6d2b8;
  }
  html, body {
    margin: 0;
    padding: 0;
    overflow: hidden;
  }
  .invitation {
    position: relative;
    width: 857px;
    height: 1200px;
    overflow: hidden;
    background: radial-gradient(ellipse at 40% 30%, var(--backdrop-light), var(--backdrop) 70%);
  }
  .ticket {
    position: absolute;
    inset: 0;
  }
  .text {
    position: absolute;
    left: 0;
    width: 857px;
    text-align: center;
    margin: 0;
    line-height: 1;
  }
  .kicker {
    top: 128px;
    font-family: "Sacramento", cursive;
    font-size: 62px;
    font-weight: 400;
    color: var(--navy);
  }
  .guest-of-honour {
    top: 206px;
    font-family: "Alfa Slab One", serif;
    font-size: 116px;
    font-weight: 400;
    color: var(--red);
    letter-spacing: 1px;
  }
  .occasion {
    top: 333px;
    font-family: "Alfa Slab One", serif;
    font-size: 61px;
    font-weight: 400;
    color: var(--navy);
    letter-spacing: 1px;
  }
  .tagline {
    top: 651px;
    font-family: "Alfa Slab One", serif;
    font-size: 35px;
    font-weight: 400;
    color: var(--white);
  }
  .field-label {
    position: absolute;
    margin: 0;
    font-family: "Comfortaa", sans-serif;
    font-weight: 500;
    font-size: 17px;
    color: var(--red);
    line-height: 1;
  }
</style>
</head>
<body>
<main class="invitation">
  <svg class="ticket" width="857" height="1200" viewBox="0 0 857 1200" xmlns="http://www.w3.org/2000/svg">
    <defs>
      <clipPath id="ticket-face">
        <path d="M186,62 L671,62 A126,126 0 0 0 789,180 L789,1023 A126,126 0 0 0 671,1141 L186,1141 A126,126 0 0 0 68,1023 L68,180 A126,126 0 0 0 186,62 Z"/>
      </clipPath>
      <linearGradient id="tan-field" x1="0" y1="0" x2="1" y2="1">
        <stop offset="0" stop-color="var(--tan)"/>
        <stop offset="1" stop-color="var(--tan-dark)"/>
      </linearGradient>
      <linearGradient id="ball-area" x1="0" y1="0" x2="0" y2="1">
        <stop offset="0" stop-color="var(--ball-light)"/>
        <stop offset="1" stop-color="var(--ball-shade)"/>
      </linearGradient>
      <linearGradient id="bat-area" x1="0" y1="0" x2="1" y2="0">
        <stop offset="0" stop-color="var(--bat-shade)"/>
        <stop offset="1" stop-color="var(--bat-light)"/>
      </linearGradient>
    </defs>

    <path class="ticket-edge" fill="var(--ticket-edge)" d="M178,54 L679,54 A118,118 0 0 0 797,172 L797,1031 A118,118 0 0 0 679,1149 L178,1149 A118,118 0 0 0 60,1031 L60,172 A118,118 0 0 0 178,54 Z"/>

    <g clip-path="url(#ticket-face)">
      <rect class="header-field" x="60" y="54" width="740" height="520" fill="url(#tan-field)"/>
      <rect class="body-field" x="60" y="626" width="740" height="530" fill="var(--cream)"/>
      <rect class="divider-band" x="60" y="574" width="740" height="52" fill="var(--band)"/>
      <line class="divider-seam" x1="60" y1="600" x2="800" y2="600" stroke="var(--white)" stroke-width="3"/>
    </g>

    <rect class="header-art" role="img" aria-label="Illustration of a large baseball rising over the divider band" x="278" y="423" width="302" height="151" fill="url(#ball-area)"/>

    <path class="ticket-frame" fill="none" stroke="var(--red)" stroke-width="5" d="M200,103 L657,103 A106,106 0 0 0 764,207 L764,989 A106,106 0 0 0 657,1100 L200,1100 A106,106 0 0 0 92,989 L92,207 A106,106 0 0 0 200,103 Z"/>

    <g class="fill-lines" stroke="var(--navy)" stroke-width="2">
      <line x1="159" y1="749" x2="697" y2="749"/>
      <line x1="159" y1="812" x2="697" y2="812"/>
      <line x1="159" y1="875" x2="413" y2="875"/>
      <line x1="443" y1="875" x2="697" y2="875"/>
      <line x1="159" y1="937" x2="697" y2="937"/>
    </g>

    <rect class="footer-art" role="img" aria-label="Illustration of a baseball bat lying with a baseball" x="231" y="971" width="398" height="95" fill="url(#bat-area)"/>
  </svg>

  <p class="text kicker">join us to celebrate</p>
  <h1 class="text guest-of-honour">ALEX’S</h1>
  <h2 class="text occasion">BIRTHDAY</h2>
  <p class="text tagline">IT’S GONNA BE FUN!</p>

  <p class="field-label" style="left:161px; top:726px;">Name</p>
  <p class="field-label" style="left:161px; top:789px;">Location</p>
  <p class="field-label" style="left:161px; top:851px;">Date</p>
  <p class="field-label" style="left:445px; top:851px;">Time</p>
  <p class="field-label" style="left:161px; top:914px;">RSVP</p>
</main>
</body>
</html>
```